My Book needs a front and back cover design

I need you to design my front and back cover of my book. The title of my book is : Beyond the Silent Pause
My Story
5 steps to speaking fluently forever

The picture that I uploaded needs to be on the front cover. On the back cover it should be excerpt from Chapter One like this :

As years have gone by I have become much more conscious about my problem with stuttering, more able to relax my muscles to alleviate it. At the age of 20, I realized that stuttering is like a demon in my head that needs to be killed and that nothing is wrong with me. Furthermore, no one can help me but myself. I'm holding the key of my future. Everything is just in my head.

With this book, I want to help you realize that nobody can help you fix your stuttering better than yourself. There's no quick-get-rid-of-stuttering cure. The cure lies inside of you.

- Lukas Orbeck, excerpt from Chapter One
----------------------------------------------------------------------------------

My name also needs to be located on the front cover.

Target Market(s)

80 million people who stutter each day

Industry/Entity Type

Psychology

Font styles to use
Serif
Sans Serif

Colors
1b1b1b
000000
333333

Requirements
Must have
• Front Cover : Full Title and subtitle and my name and my picture
• Back Cover : Excerpt from my Chapter One with my name below just as I have described in my project description
Nice to have
• Maybe black background would be the best for the front cover.

```html
<!DOCTYPE html>
<html lang="en">
<head>
<meta charset="utf-8">
<title>Beyond the Silent Pause – Cover Spread</title>
<link rel="stylesheet" href="https://fonts.googleapis.com/css2?family=Archivo:wght@800&family=Tenor+Sans&family=EB+Garamond:wght@400&family=Arimo:wght@400;700&display=swap">
<style>
  :root {
    --stage: #e4e4e4;
    --cover-dark: #1b1b1b;
    --cover-black: #000000;
    --cover-mid: #333333;
    --ink-white: #ffffff;
    --title-silver-top: #ffffff;
    --title-silver-bottom: #b9bcc2;
    --title-red-top: #e2262d;
    --title-red-bottom: #a5070c;
    --spine-red: #c8151b;
    --code-box: #b3b4b8;
    --portrait-frame: #2a2a2a;
  }
  * { margin: 0; padding: 0; box-sizing: border-box; }
  html, body { width: 1200px; height: 595px; overflow: hidden; }
  body { background: var(--stage); position: relative; }

  .cover-spread {
    position: absolute;
    left: 221px; top: 10px;
    width: 758px; height: 575px;
    background:
      radial-gradient(ellipse at 50% 40%, var(--cover-mid) 0%, var(--cover-dark) 55%, var(--cover-black) 100%);
    overflow: hidden;
    color: var(--ink-white);
  }

  /* Back cover */
  .back-cover { position: absolute; left: 0; top: 0; width: 360px; height: 100%; }
  .author-portrait-small {
    position: absolute; left: 26px; top: 79px; width: 115px; height: 131px;
    border: 2px solid var(--portrait-frame);
    background: radial-gradient(ellipse at 50% 38%, #6b5a52 0%, #3a3230 35%, #141414 75%);
  }
  .excerpt {
    font-family: "Arimo", Arial, sans-serif;
    font-weight: 700;
    font-size: 8.6px;
    line-height: 13.4px;
  }
  .excerpt-lead { position: absolute; left: 147px; top: 111px; width: 205px; }
  .excerpt-close { position: absolute; left: 44px; top: 233px; width: 310px; text-align: center; }
  .excerpt-credit { position: absolute; left: 86px; top: 286px; }
  .code-box { position: absolute; left: 134px; top: 303px; width: 134px; height: 83px; background: var(--code-box); }

  /* Spine */
  .spine-title {
    position: absolute; left: 388px; top: 166px;
    writing-mode: vertical-rl;
    font-family: "Arimo", Arial, sans-serif; font-weight: 700;
    font-size: 12px; letter-spacing: 0.5px; white-space: nowrap;
  }
  .spine-title .accent { color: var(--spine-red); }

  /* Front cover */
  .front-cover { position: absolute; left: 400px; top: 0; width: 358px; height: 100%; text-align: center; }
  .author-portrait-large {
    position: absolute; left: 10px; top: 222px; width: 328px; height: 353px;
    background:
      radial-gradient(ellipse 38% 30% at 50% 32%, #7a675e 0%, #4a3d38 45%, transparent 80%),
      radial-gradient(ellipse 70% 45% at 50% 100%, #0a0a0a 0%, #111 60%, transparent 100%);
  }
  .book-title { position: absolute; left: 0; top: 62px; width: 100%; font-family: "Archivo", Arial, sans-serif; font-weight: 800; }
  .book-title .line { display: block; line-height: 42px; -webkit-background-clip: text; background-clip: text; color: transparent; }
  .book-title .silver { font-size: 34px; background-image: linear-gradient(var(--title-silver-top) 30%, var(--title-silver-bottom)); }
  .book-title .red { font-size: 36px; background-image: linear-gradient(var(--title-red-top) 30%, var(--title-red-bottom)); }
  .book-subtitle-main {
    position: absolute; left: 0; top: 156px; width: 100%;
    font-family: "Tenor Sans", sans-serif; font-size: 27px; color: #e9e9ec;
  }
  .book-tagline {
    position: absolute; left: 0; top: 197px; width: 100%;
    font-family: "EB Garamond", serif; font-size: 15px;
  }
  .author-name {
    position: absolute; left: 0; top: 531px; width: 100%;
    font-family: "Tenor Sans", sans-serif; font-size: 22px;
  }
</style>
</head>
<body>
  <main class="cover-spread">
    <section class="back-cover">
      <div class="author-portrait-small" role="img" aria-label="Portrait photo of the author"></div>
      <p class="excerpt excerpt-lead">As years have gone by I have become much more conscious about my problem with stuttering, more able to relax my muscles to alleviate it. At the age of 20, I realized that stuttering is like a demon in my head that needs to be killed and that nothing is wrong with me. Furthermore, no one can help me but myself. I'm holding the key of my future. Everything is just in my head.</p>
      <p class="excerpt excerpt-close">With this book, I want to help you realize that nobody can help you fix your stuttering better than yourself. There's no quick-get-rid-of-stuttering cure. The cure lies inside of you.</p>
      <p class="excerpt excerpt-credit">- Lukas Orbeck, excerpt from Chapter One</p>
      <div class="code-box"></div>
    </section>

    <div class="spine-title">BEYOND THE <span class="accent">SILENT PAUSE:</span> MY STORY</div>

    <section class="front-cover">
      <div class="author-portrait-large" role="img" aria-label="Portrait photo of the author in a dark polo shirt"></div>
      <h1 class="book-title">
        <span class="line silver">BEYOND THE</span>
        <span class="line red">SILENT PAUSE</span>
      </h1>
      <p class="book-subtitle-main">MY STORY</p>
      <p class="book-tagline">5 steps to speaking fluently forever</p>
      <p class="author-name">Lukas Orbeck</p>
    </section>
  </main>
</body>
</html>
```